COMPANY SIGN

I am in the process of ordering new company For Sale signs and stationary (business cards, envelopes, letterheads, and labels). I need a new design with my existing company logo. The TWO MOST IMPORTANT PROJECTS I need right now is the new design for the company sign and business cards. I've uploaded a .jpg file of my company logo.

I like the design to be eye catching and the background color of the company sign to be soothing to the eyes. Perhaps, using one of the color on the leaves of the logo or any other color that the designer think will go well with the logo. My favorite colors are teal or light olive color but don't let that affect your creativity.

Industry/Entity Type

Business

Requirements
Should not have
• Please don't use "Times New Roman" fonts or fonts that is hard to read.

```html
<!DOCTYPE html>
<html lang="en">
<head>
<meta charset="utf-8">
<title>Maplewood House Walk – Business Card</title>
<link rel="stylesheet" href="https://fonts.googleapis.com/css2?family=Arimo:wght@700&family=Open+Sans:wght@300;400&display=swap">
<style>
  :root {
    --page-bg: #ffffff;
    --label-ink: #000000;
    --card-teal: #00918a;
    --band-green: #8dc63f;
    --card-ink: #ffffff;
    --mark-fill: #f4c51c;
  }
  * { box-sizing: border-box; margin: 0; padding: 0; }
  html, body {
    width: 932px;
    height: 1200px;
    overflow: hidden;
    background: var(--page-bg);
  }
  .sheet {
    position: relative;
    width: 932px;
    height: 1200px;
  }
  .side-label {
    position: absolute;
    left: 0;
    width: 100%;
    text-align: center;
    font-family: "Arimo", Arial, sans-serif;
    font-weight: 700;
    font-size: 48px;
    color: var(--label-ink);
    line-height: 1;
  }
  .side-label--front { top: 6px; }
  .side-label--back { top: 644px; }

  .card {
    position: absolute;
    left: 81px;
    width: 776px;
    height: 432px;
    background: var(--card-teal);
    overflow: hidden;
  }
  .card--front { top: 82px; }
  .card--back { top: 715px; }

  .brand__dot {
    position: absolute;
    left: 50%;
    border-radius: 50%;
    background: var(--mark-fill);
    transform: translateX(-50%);
  }
  .brand__name {
    position: absolute;
    left: 0;
    width: 100%;
    text-align: center;
    font-family: "Open Sans", Arial, sans-serif;
    font-weight: 300;
    color: var(--card-ink);
    white-space: nowrap;
    line-height: 1;
  }
  .card--front .brand__dot { top: 84px; width: 136px; height: 136px; }
  .card--front .brand__name { top: 262px; font-size: 56px; }

  .card--back .brand__dot { top: 40px; width: 90px; height: 90px; }
  .card--back .brand__name { top: 152px; font-size: 38px; }

  .contact-band {
    position: absolute;
    left: 0;
    bottom: 0;
    width: 100%;
    height: 158px;
    background: var(--band-green);
    font-family: "Open Sans", Arial, sans-serif;
    color: var(--card-ink);
  }
  .holder {
    position: absolute;
    left: 18px;
    top: 18px;
  }
  .holder__name {
    font-size: 35px;
    font-weight: 400;
    line-height: 1.1;
  }
  .holder__role {
    font-size: 15px;
    margin-left: 8px;
    line-height: 1.3;
  }
  .details {
    position: absolute;
    right: 26px;
    top: 28px;
    text-align: right;
    font-size: 25px;
    line-height: 1.42;
    list-style: none;
  }
</style>
</head>
<body>
<main class="sheet">
  <h2 class="side-label side-label--front">FRONT</h2>
  <section class="card card--front">
    <span class="brand__dot"></span>
    <span class="brand__name">Maplewood House Walk</span>
  </section>

  <h2 class="side-label side-label--back">BACK</h2>
  <section class="card card--back">
    <span class="brand__dot"></span>
    <span class="brand__name">Maplewood House Walk</span>
    <div class="contact-band">
      <div class="holder">
        <p class="holder__name">Your Name Here</p>
        <p class="holder__role">position</p>
      </div>
      <ul class="details">
        <li>1011 Street, Homeland</li>
        <li>123-456-789</li>
        <li>your@email.com</li>
      </ul>
    </div>
  </section>
</main>
</body>
</html>
```